877 stay Bold

Redesigning this front and back business card flyer and keeping the info but making it look better.

This is all about using the info and logo on the business card design and creating a better layout using any of the following and more.

Changing the background color or imagine, chaining the placement of content, resizing content.

Target Market(s)

Targeting people that have been injured on one side and people that have been giving a DUI on the other.

Contact Information for Business Card

We are looking to keep the info but make it look a fee cleaner and less cluttered

Font styles to use
Sans Serif

Requirements
Must have
• Must have the same info but a better layout.
Nice to have
• better background colors or image or layout. different fonts or same font all design options that will make it look professional and clean.

```html
<!DOCTYPE html>
<html lang="en">
<head>
<meta charset="utf-8">
<title>877 Stay Bold – Business Cards</title>
<link rel="stylesheet" href="https://fonts.googleapis.com/css2?family=Archivo+Black&family=Arimo:wght@400;700&display=swap">
<style>
  :root {
    --ink: #0b0b0b;
    --red: #d5202a;
    --red-deep: #b91c24;
    --white: #ffffff;
    --paper: #f4f4f4;
    --stage-top: #e9eaec;
    --stage-bottom: #b9bbbf;
    --text-dark: #161616;
  }
  * { box-sizing: border-box; margin: 0; padding: 0; }
  html, body { width: 1200px; height: 800px; overflow: hidden; }
  body {
    background: linear-gradient(160deg, var(--stage-top), var(--stage-bottom));
    font-family: "Arimo", Arial, sans-serif;
    position: relative;
  }
  .card {
    position: absolute;
    width: 620px;
    height: 354px;
    overflow: hidden;
    box-shadow: 0 10px 28px rgba(0,0,0,.28);
  }
  .card--injury { left: 470px; top: 40px; background: var(--ink); color: var(--white); }
  .card--dui { left: 110px; top: 410px; background: var(--paper); color: var(--text-dark); }

  /* brand lockup */
  .brand-strip {
    position: absolute; top: 0; bottom: 0; width: 74px;
    display: flex; align-items: center; justify-content: center;
    background: var(--ink);
  }
  .brand-name {
    font-family: "Archivo Black", Arial, sans-serif;
    color: var(--white);
    font-size: 30px;
    letter-spacing: 1px;
    white-space: nowrap;
  }
  .card--injury .brand-strip { left: 0; }
  .card--injury .brand-name { transform: rotate(90deg); }
  .card--dui .brand-strip { right: 0; }
  .card--dui .brand-name { transform: rotate(-90deg); }

  /* injury card content */
  .injury-body { position: absolute; left: 88px; top: 22px; width: 390px; }
  .injury-kicker { font-family: "Archivo Black", Arial, sans-serif; font-size: 22px; line-height: 1.1; }
  .injury-title { font-family: "Archivo Black", Arial, sans-serif; font-size: 34px; color: var(--red); line-height: 1.05; margin-bottom: 8px; }
  .reasons { list-style: none; font-size: 14px; line-height: 1.3; margin-bottom: 10px; }
  .reasons li, .dui-tips li { position: relative; padding-left: 14px; }
  .reasons li::before, .dui-tips li::before {
    content: ""; position: absolute; left: 0; top: 4px;
    border-left: 8px solid var(--red);
    border-top: 5px solid transparent; border-bottom: 5px solid transparent;
  }
  .promise { font-weight: 700; font-size: 16px; line-height: 1.2; margin-bottom: 10px; }

  .contact-phone {
    display: flex; align-items: center; gap: 10px;
    font-weight: 700; font-size: 30px; line-height: 1;
  }
  .phone-icon { width: 28px; height: 28px; flex: none; }
  .contact-web { font-size: 18px; margin-top: 6px; }

  .injury-photos {
    position: absolute; right: 14px; top: 14px; bottom: 14px; width: 128px;
    display: flex; flex-direction: column; gap: 6px;
  }
  .photo { flex: 1; }
  .photo--crash { background: linear-gradient(135deg, #3a1a2a, #7a6a78 55%, #1c1a22); }
  .photo--crutch { background: linear-gradient(180deg, #9a9a9a, #cfcfcf 60%, #7a7a7a); }
  .photo--wheelchair { background: linear-gradient(90deg, #1a1a1a, #5a5d62 60%, #222); }

  /* dui card content */
  .dui-panel {
    position: absolute; left: 0; top: 0; bottom: 0; width: 250px;
    background: var(--red);
  }
  .dui-title {
    position: absolute; left: 20px; top: 22px;
    font-family: "Archivo Black", Arial, sans-serif;
    color: var(--white); font-size: 34px; line-height: 1.0;
  }
  .dui-art {
    position: absolute; left: 0; right: 0; bottom: 0; height: 190px;
    background: linear-gradient(160deg, var(--red), var(--red-deep));
  }
  .dui-body { position: absolute; left: 264px; top: 18px; width: 272px; }
  .dui-question { font-weight: 700; font-size: 18px; line-height: 1.15; margin-bottom: 6px; }
  .dui-tips { list-style: none; font-size: 12.5px; line-height: 1.22; margin-bottom: 10px; }
  .card--dui .contact-phone { font-size: 28px; }
  .card--dui .contact-web { font-size: 16px; }
</style>
</head>
<body>

<section class="card card--injury">
  <div class="brand-strip"><span class="brand-name">877 STAY BOLD</span></div>
  <div class="injury-body">
    <p class="injury-kicker">If You’ve Been Injured</p>
    <h1 class="injury-title">STAY BOLD</h1>
    <ul class="reasons">
      <li>for an inexperienced lawyer!</li>
      <li>for less than you deserve!</li>
      <li>for paying massive medical bills!</li>
      <li>for a life of pain and debt!</li>
    </ul>
    <p class="promise">We fight for you, so you<br>can focus on getting better</p>
    <p class="contact-phone">
      <svg class="phone-icon" viewBox="0 0 28 28" aria-hidden="true"><circle cx="14" cy="14" r="14" fill="#d5202a"/><path d="M9.5 7.5l3 3-1.6 1.8c.9 1.9 2.4 3.5 4.3 4.4l1.8-1.6 3 3-2 2c-5.2-.6-9.9-5.3-10.5-10.5z" fill="#fff"/></svg>
      877-555-0142
    </p>
    <p class="contact-web">www.877staybold.com</p>
  </div>
  <div class="injury-photos">
    <div class="photo photo--crash" role="img" aria-label="Photo of a crashed car at night with emergency lights"></div>
    <div class="photo photo--crutch" role="img" aria-label="Photo of a leg in a walking boot with crutches"></div>
    <div class="photo photo--wheelchair" role="img" aria-label="Photo of a person in a wheelchair by a window"></div>
  </div>
</section>

<section class="card card--dui">
  <div class="dui-panel">
    <div class="dui-art" role="img" aria-label="Illustration of a judge's gavel"></div>
    <h2 class="dui-title">STAY BOLD<br>FOR A<br>DUI</h2>
  </div>
  <div class="dui-body">
    <p class="dui-question">What Should I Do If I Get Pulled Over For Dui?</p>
    <ul class="dui-tips">
      <li>Pull over in a calm, normal manner</li>
      <li>Be polite at all times</li>
      <li>Do not admit to drinking</li>
      <li>Do not submit to any field sobriety tests</li>
      <li>Do not submit to taking a chemical test (breath, blood or urine)</li>
      <li>Do not make any statement after being arrested, especially when placed in the police cruiser</li>
    </ul>
    <p class="contact-phone">
      <svg class="phone-icon" viewBox="0 0 28 28" aria-hidden="true"><circle cx="14" cy="14" r="14" fill="#d5202a"/><path d="M9.5 7.5l3 3-1.6 1.8c.9 1.9 2.4 3.5 4.3 4.4l1.8-1.6 3 3-2 2c-5.2-.6-9.9-5.3-10.5-10.5z" fill="#fff"/></svg>
      877-555-0142
    </p>
    <p class="contact-web">www.877staybold.com</p>
  </div>
  <div class="brand-strip"><span class="brand-name">877 STAY BOLD</span></div>
</section>

</body>
</html>
```